Professional Coaching Business Letterhead/Footer

I need a letterhead and email footer for my personal coaching business, Dorian K Falstead Professional Coaching. I send several attachments to new clients (such as welcome letter, fee structure, etc) and would like these pages to have my branding on them.
I prefer the black and gold/silver color scheme, and will attach my logo to be used. I'd like the overall impression to be upmarket/regal/professional.

One of the uploaded files is my business card, to give an idea of the style/feel I like. The others are vector files containing logo to be used.

Target Market(s)

Corporate managers, successful business people. 30-60 yrs old.

Industry/Entity Type

Business

Requirements
Must have
• Logo (DKF)
Nice to have
• Shield emblem around logo, some type of watermark.
Should not have
• The first uploaded file is my business card, intended to show style and colors- not to be used itself as the letterhead.

```html
<!DOCTYPE html>
<html lang="en">
<head>
<meta charset="utf-8">
<title>Dorian K Falstead Professional Coaching – Letterhead</title>
<link rel="stylesheet" href="https://fonts.googleapis.com/css2?family=Josefin+Sans:wght@300;400;600&display=swap">
<style>
  :root {
    --ink: #111111;
    --paper: #ffffff;
    --gold-light: #f7d41c;
    --gold-deep: #f08c00;
    --silver: #b5b5b5;
    --silver-light: #eeeeee;
    --watermark: #f6dfae;
    --watermark-soft: #fbecc8;
  }
  html, body {
    margin: 0;
    padding: 0;
    overflow: hidden;
    background: var(--paper);
  }
  .letterhead {
    position: relative;
    width: 858px;
    height: 1200px;
    background: var(--paper);
    overflow: hidden;
    font-family: "Josefin Sans", sans-serif;
  }
  .letterhead__decor {
    position: absolute;
    inset: 0;
  }
  .header-flourish {
    position: absolute;
    left: 456px;
    top: 66px;
    width: 172px;
    height: 86px;
    border-radius: 50%;
    background: radial-gradient(ellipse at center, rgba(247,212,28,0.45), rgba(240,140,0,0.2) 55%, rgba(255,255,255,0) 75%);
  }
  .footer-flourish {
    position: absolute;
    left: 738px;
    top: 1010px;
    width: 84px;
    height: 90px;
    border-radius: 50%;
    background: radial-gradient(ellipse at center, rgba(247,212,28,0.45), rgba(247,212,28,0.15) 55%, rgba(255,255,255,0) 75%);
  }
  .brand {
    position: absolute;
    left: 618px;
    top: 60px;
    width: 160px;
    text-align: center;
  }
  .brand__badge {
    width: 106px;
    height: 106px;
    margin: 0 auto;
    border: 6px solid var(--ink);
    border-radius: 50%;
    box-sizing: border-box;
    display: flex;
    align-items: center;
    justify-content: center;
    font-size: 30px;
    font-weight: 600;
    color: var(--ink);
    letter-spacing: 1px;
    padding-top: 4px;
  }
  .brand__name {
    margin-top: 14px;
    font-size: 14px;
    font-weight: 600;
    color: var(--ink);
    letter-spacing: 0.5px;
    white-space: nowrap;
  }
  .watermark {
    position: absolute;
    left: 0;
    top: 0;
    width: 858px;
    height: 1200px;
    pointer-events: none;
  }
  .watermark__ring {
    position: absolute;
    left: 274px;
    top: 408px;
    width: 310px;
    height: 310px;
    border: 9px solid var(--watermark-soft);
    border-radius: 50%;
    box-sizing: border-box;
    display: flex;
    align-items: center;
    justify-content: center;
    font-size: 110px;
    font-weight: 400;
    color: var(--watermark);
    padding-top: 12px;
  }
  .watermark__name {
    position: absolute;
    left: 0;
    width: 858px;
    top: 764px;
    text-align: center;
    font-size: 40px;
    line-height: 44px;
    font-weight: 300;
    color: var(--watermark);
    letter-spacing: 1px;
  }
  .watermark__flourish {
    position: absolute;
    top: 762px;
    width: 110px;
    height: 46px;
    border-radius: 50%;
    background: radial-gradient(ellipse at center, rgba(246,223,174,0.6), rgba(255,255,255,0) 70%);
  }
  .watermark__flourish--left { left: 108px; }
  .watermark__flourish--right { left: 640px; }
</style>
</head>
<body>
<main class="letterhead">
  <svg class="letterhead__decor" width="858" height="1200" viewBox="0 0 858 1200" aria-hidden="true">
    <defs>
      <linearGradient id="gold-bar" x1="0" x2="1">
        <stop offset="0" stop-color="#f7d41c"/>
        <stop offset="1" stop-color="#f08c00"/>
      </linearGradient>
      <linearGradient id="silver-bar" x1="0" x2="1">
        <stop offset="0" stop-color="#9a9a9a"/>
        <stop offset="1" stop-color="#eeeeee"/>
      </linearGradient>
      <linearGradient id="silver-wave" x1="0" x2="1">
        <stop offset="0" stop-color="#9c9c9c"/>
        <stop offset="0.6" stop-color="#eeeeee"/>
        <stop offset="1" stop-color="#ffffff"/>
      </linearGradient>
      <linearGradient id="ink-wave" x1="0" x2="1">
        <stop offset="0" stop-color="#333333"/>
        <stop offset="1" stop-color="#000000"/>
      </linearGradient>
    </defs>

    <rect class="frame" x="33" y="41" width="792" height="1132" fill="none" stroke="#111" stroke-width="2"/>

    <rect class="header-bar header-bar--gold" x="33" y="103" width="412" height="10" fill="url(#gold-bar)"/>
    <rect class="header-bar header-bar--silver" x="768" y="104" width="70" height="8" fill="url(#silver-bar)"/>

    <path class="footer-wave footer-wave--silver" d="M33,1173 L33,1140 C200,1112 450,1106 640,1100 C730,1096 790,1084 825,1062 L825,1173 Z" fill="url(#silver-wave)"/>
    <path class="footer-wave footer-wave--gold-line" d="M33,1134 C220,1100 460,1094 640,1090 C720,1087 790,1074 825,1052" fill="none" stroke="#f08c00" stroke-width="4"/>
    <path class="footer-wave footer-wave--ink" d="M33,1173 L33,1172 C250,1160 480,1142 640,1126 C740,1114 800,1098 825,1074 L825,1173 Z" fill="url(#ink-wave)"/>
  </svg>

  <div class="header-flourish" role="img" aria-label="Gold flourish ornament"></div>
  <div class="footer-flourish" role="img" aria-label="Gold curl ornament"></div>

  <header class="brand">
    <div class="brand__badge">DKF</div>
    <div class="brand__name">DORIAN K FALSTEAD</div>
  </header>

  <div class="watermark" aria-hidden="true">
    <div class="watermark__ring">DKF</div>
    <div class="watermark__flourish watermark__flourish--left"></div>
    <div class="watermark__name">DORIAN K FALSTEAD</div>
    <div class="watermark__flourish watermark__flourish--right"></div>
  </div>
</main>
</body>
</html>
```